Brivane Communications - veteran and exclusive boutique copywriting agency

PROJECT NEEDS:
1. Website design - full homepage design and inner page top banner design
2. Logo design
* Please see attached Briefs (Word Docs) for descriptions of what is needed for 1 and 2 above.
ABOUT THE CLIENT:
Brivane Communications is a veteran and exclusive boutique copywriting agency run by Martin Olafsky. Martin is an award-winning published novelist and an accomplished executive ghostwriter with articles regularly published prominent technology publications like Pulsar, ByteHarbor, CapitalDrift, and more. For nearly three decades, Martin has focused solely on the technology sector - serving clients in Israel, Europe and the US.

Target Market(s)

hi-tech companies run by serious, confident professionals.

Industry/Entity Type

Business

Number of Pages Required

2 page

Font styles to use
Sans Serif
Other font styles liked:
• font should be modern

Colors
0054AA
0677BA
7BADD7
CADEEF
E8F1F8
F0912C
F2A743
F7CA91
FBE8D2
FDF5EE

Requirements
Must have
• psd files for logo, homepage design, and inner page top banner design
Nice to have
• Please see attached Website and Logo Design Briefs (Word Docs)
Should not have

```html
<!DOCTYPE html>
<html lang="en">
<head>
<meta charset="utf-8">
<title>Brivane Communications</title>
<link rel="stylesheet" href="https://fonts.googleapis.com/css2?family=Alegreya+Sans:wght@500;700;800&family=Lato:wght@400;700&display=swap">
<style>
:root{
  --ink:#111114;
  --hero:#1a1c22;
  --red:#d13a1e;
  --band:#d3432a;
  --navy:#1d3f8a;
  --link:#1d3f8a;
  --white:#ffffff;
  --text:#222;
  --muted:#c9c9c9;
  --star:#f0912c;
}
*{box-sizing:border-box;margin:0;padding:0}
html,body{width:1200px;height:3147px;overflow:hidden}
body{position:relative;background:var(--white);font-family:"Lato",sans-serif;color:var(--text)}
.abs{position:absolute}
.head{font-family:"Alegreya Sans",sans-serif;font-weight:800}
.btn{position:absolute;display:flex;align-items:center;justify-content:center;background:var(--red);color:var(--white);font-family:"Alegreya Sans",sans-serif;font-weight:800;font-size:18px;border-radius:2px;box-shadow:0 3px 6px rgba(0,0,0,.2)}

/* hero */
.hero{position:absolute;left:0;top:0;width:1200px;height:690px}
.logo{position:absolute;color:var(--white);font-family:"Alegreya Sans",sans-serif;font-weight:800;line-height:1}
.nav{position:absolute;top:32px;left:386px;display:flex;gap:47px;color:var(--white);font-size:16px}
.hero-photo{position:absolute;left:758px;top:70px;width:345px;height:610px;background:radial-gradient(ellipse at 50% 35%,#9bb3d6 0%,#6b84aa 40%,rgba(40,48,64,0) 75%)}
.hero h1{position:absolute;left:97px;top:230px;font-size:60px;color:var(--white);font-family:"Alegreya Sans",sans-serif;font-weight:800;letter-spacing:-.5px}
.hero p{position:absolute;left:97px;top:316px;width:480px;font-size:17px;line-height:31px;color:var(--white)}

/* services */
.section-title{position:absolute;width:1200px;text-align:center;font-family:"Alegreya Sans",sans-serif;font-weight:800;font-size:42px;color:var(--ink)}
.section-title span{color:var(--red)}
.card{position:absolute;top:816px;width:326px;height:571px;background:var(--white);box-shadow:0 2px 8px rgba(0,0,0,.15);border-radius:4px;text-align:center}
.card-img{width:326px;height:262px;border-radius:4px 4px 0 0}
.card-icon{position:absolute;left:121px;top:227px;width:84px;height:84px;border-radius:50%;background:var(--white);box-shadow:0 2px 6px rgba(0,0,0,.2);display:flex;align-items:center;justify-content:center}
.card h3{position:absolute;top:323px;width:100%;font-family:"Alegreya Sans",sans-serif;font-weight:700;font-size:27px;color:var(--ink)}
.card h4{position:absolute;top:361px;width:100%;font-weight:400;font-size:16px;color:var(--link)}
.card p{position:absolute;top:390px;left:20px;width:286px;font-size:15px;line-height:31px}
.card .btn{left:96px;top:487px;width:133px;height:53px}

/* why */
.band{position:absolute;left:0;top:1526px;width:1200px;height:559px;background:var(--band)}
.why-frame{position:absolute;left:110px;top:1490px;width:445px;height:657px;border:3px solid var(--navy)}
.why-photo{position:absolute;left:98px;top:1477px;width:441px;height:655px;background:radial-gradient(ellipse at 50% 45%,#8fa7cc 0%,#4b5a75 35%,#1c1f27 75%)}
.why h2{position:absolute;left:566px;top:1578px;font-size:42px;color:var(--white)}
.why p{position:absolute;left:566px;top:1635px;width:540px;font-size:15px;line-height:31px;color:var(--white)}
.btn.outline{background:transparent;border:3px solid var(--white);border-radius:5px;box-shadow:none}

/* testimonials */
.quote{position:absolute;left:210px;top:2281px;width:780px;text-align:center;font-size:17px;line-height:30px;color:#333}
.arrow{position:absolute;top:2290px;width:42px;height:42px}
.avatar{position:absolute;top:2451px;width:100px;height:100px;border-radius:50%;border:4px solid #7f9ac4;background:radial-gradient(circle at 50% 45%,#c9b79f 0%,#aab5c6 60%,#e3e7ee 100%)}
.avatar.active{border-color:var(--navy);opacity:1}
.avatar.faded{opacity:.7}
.name{position:absolute;top:2574px;width:1200px;text-align:center;font-size:16px;color:var(--ink)}

/* footer */
.footer{position:absolute;left:0;top:2752px;width:1200px;height:395px;background:var(--ink);color:var(--white)}
.footer h5{position:absolute;font-family:"Alegreya Sans",sans-serif;font-weight:800;font-size:21px}
.footer .small{position:absolute;font-size:15px;line-height:31px}
.vline{position:absolute;top:85px;width:1px;height:170px;background:#555}
.contact-row{position:absolute;left:562px;display:flex;align-items:center;gap:12px;font-size:15px}
.email{position:absolute;left:877px;top:184px;width:225px;height:53px;border:1px solid #ddd;border-radius:3px;display:flex;overflow:hidden}
.email span{flex:1;padding-left:16px;line-height:51px;font-size:15px}
.email b{width:52px;background:#2a5aa0;display:flex;align-items:center;justify-content:center}
.copyright{position:absolute;top:350px;width:1200px;text-align:center;font-size:15px}
</style>
</head>
<body>

<section class="hero">
  <svg class="abs" width="1200" height="690" style="left:0;top:0">
    <defs><radialGradient id="heroGlow" cx="75%" cy="30%" r="70%"><stop offset="0" stop-color="#3b414d"/><stop offset="1" stop-color="#15161b"/></radialGradient></defs>
    <path d="M0 0H1200V628Q1100 660 900 680Q500 690 0 672Z" fill="url(#heroGlow)"/>
  </svg>
  <div class="hero-photo" role="img" aria-label="Portrait of Martin Olafsky in a light blue shirt and jeans"></div>
  <div class="logo" style="left:98px;top:12px;font-size:40px">Brivane<div style="font-size:13px;letter-spacing:.5px;margin-top:2px">COMMUNICATIONS</div></div>
  <nav class="nav"><span>Home</span><span>About</span><span>Services</span><span>Industries</span><span>Portfolio</span><span>Clients</span><span>Contact</span></nav>
  <svg class="abs" style="left:1075px;top:32px" width="22" height="22" viewBox="0 0 22 22" fill="none" stroke="#fff" stroke-width="2"><circle cx="9" cy="9" r="7"/><path d="M14 14l6 6"/></svg>
  <h1>Your voice, my words.</h1>
  <p>Copywriting and executive ghostwriting that speaks for your vision and your technology.</p>
  <div class="btn" style="left:98px;top:390px;width:133px;height:51px">Get Started</div>
</section>

<h2 class="section-title" style="top:745px">What <span>I do</span></h2>

<article class="card" style="left:98px">
  <div class="card-img" role="img" aria-label="Hands using a phone with glowing chat bubbles" style="background:linear-gradient(135deg,#1d2a30,#2f6f78 55%,#6a4c36)"></div>
  <div class="card-icon"><svg width="46" height="46" viewBox="0 0 46 46" fill="none" stroke="#d13a1e" stroke-width="2.5"><path d="M23 6c10 0 17 6 17 14s-7 14-17 14c-2 0-4 0-6-1l-8 5 2-7c-3-3-5-6-5-11C6 12 13 6 23 6z"/><path d="M15 17h16M15 22h16M15 27h10" stroke="#1d3f8a"/></svg></div>
  <h3>Messaging</h3>
  <h4>The Value of a Fresh Perspective</h4>
  <p>Could you be reaching farther? Clearly-defined, accurately-targeted messaging is crucial.</p>
  <div class="btn">Read More</div>
</article>

<article class="card" style="left:437px">
  <div class="card-img" role="img" aria-label="Circuit board with a chip held by tweezers" style="background:linear-gradient(135deg,#5c7f9a,#2e4a5e 50%,#9fb4c4)"></div>
  <div class="card-icon"><svg width="46" height="46" viewBox="0 0 46 46" fill="none" stroke="#1d3f8a" stroke-width="2.2"><rect x="8" y="6" width="24" height="30" rx="2"/><path d="M12 12h6v5h-6zM21 13h8M12 22h16M12 27h10"/><circle cx="34" cy="30" r="7" stroke="#d13a1e"/><path d="M6 40h20" stroke="#d13a1e"/></svg></div>
  <h3>Collateral</h3>
  <h4>Concise, Effective, Creative</h4>
  <p>Marketing collateral that effectively communicates who you are and what you want to say.</p>
  <div class="btn">Read More</div>
</article>

<article class="card" style="left:776px">
  <div class="card-img" role="img" aria-label="Businessman holding a tablet with floating network icons" style="background:linear-gradient(135deg,#0f2233,#1f4258 55%,#0c1a26)"></div>
  <div class="card-icon"><svg width="46" height="46" viewBox="0 0 46 46" fill="none" stroke="#1d3f8a" stroke-width="2.2"><rect x="6" y="6" width="16" height="14" rx="2"/><path d="M8 17l5-5 4 4 3-2"/><rect x="25" y="6" width="14" height="18" rx="2"/><path d="M28 11h8M28 15h8M28 19h6"/><rect x="23" y="28" width="17" height="12" rx="2" stroke="#d13a1e"/><path d="M30 31v6l4-3z" stroke="#d13a1e"/><path d="M8 30c0-3 3-5 6-5s6 2 6 5-3 5-6 5l-4 3 1-4c-2-1-3-2-3-4z" stroke="#d13a1e"/></svg></div>
  <h3>Content Marketing</h3>
  <h4>Giving Voice to Your Vision</h4>
  <p>Articles, blog content, white papers, e-books. Your ideas and expertise, our words.</p>
  <div class="btn">Read More</div>
</article>

<section class="why">
  <div class="band"></div>
  <div class="why-frame"></div>
  <div class="why-photo" role="img" aria-label="Portrait of Martin Olafsky standing with hands in pockets"></div>
  <h2 class="head">Why choose me</h2>
  <p>Sed ut perspiciatis unde omnis iste natus error sit voluptatem accusantium doloremque laudantium, totam rem aperiam, eaque ipsa quae ab illo inventore veritatis et quasi architecto beatae vitae dicta sunt explicabo. Nemo enim ipsam voluptatem quia voluptas sit aspernatur aut odit aut fugit, sed quia consequuntur magni dolores eos qui ratione voluptatem sequi nesciunt. Neque porro quisquam est, qui dolorem ipsum quia dolor sit amet, consectetur, adipisci velit, sed quia non numquam eius modi tempora incidunt ut labore et dolore magnam aliquam quaerat voluptatem. Ut enim ad minima veniam, quis nostrum exercitationem ullam corporis suscipit laboriosam, nisi ut aliquid ex ea commodi consequatur?</p>
  <div class="btn outline" style="left:565px;top:1961px;width:137px;height:57px">Read More</div>
</section>

<section class="testimonials">
  <h2 class="section-title" style="top:2202px">What they’re <span>saying</span></h2>
  <svg class="arrow" style="left:34px" viewBox="0 0 42 42" fill="none" stroke="#555" stroke-width="2"><circle cx="21" cy="21" r="19"/><path d="M24 12l-9 9 9 9"/></svg>
  <svg class="arrow" style="left:1124px" viewBox="0 0 42 42" fill="none" stroke="#111" stroke-width="2.5"><circle cx="21" cy="21" r="19"/><path d="M18 12l9 9-9 9"/></svg>
  <p class="quote">“Sed ut perspiciatis unde omnis iste natus error sit voluptatem accusantium doloremque laudantium, totam rem aperiam, eaque ipsa quae ab illo inventore veritatis et quasi architecto beatae vitae dicta sunt explicabo.”</p>
  <svg class="abs" style="left:540px;top:2393px" width="120" height="22" viewBox="0 0 120 22" fill="#f0912c">
    <path id="st" d="M11 1l3 7 7 .6-5.4 4.6 1.7 7.1L11 16.5 4.7 20.3l1.7-7.1L1 8.6 8 8z"/>
    <use href="#st" x="24"/><use href="#st" x="48"/><use href="#st" x="72"/><use href="#st" x="96"/>
  </svg>
  <div class="avatar faded" style="left:428px" role="img" aria-label="Client portrait"></div>
  <div class="avatar active" style="left:549px" role="img" aria-label="Client portrait"></div>
  <div class="avatar faded" style="left:670px" role="img" aria-label="Client portrait"></div>
  <div class="name">DANA WHITFIELD</div>
  <div class="btn" style="left:532px;top:2622px;width:138px;height:51px">Learn More</div>
</section>

<footer class="footer">
  <div class="logo" style="left:98px;top:66px;font-size:58px">Brivane<div style="font-size:19px;letter-spacing:.5px;margin-top:2px">COMMUNICATIONS</div></div>
  <p class="small" style="left:98px;top:168px;width:370px">Lorem ipsum dolor sit amet, consectetur adipiscing elit, sed do eiusmod tempor incididunt ut labore et dolore magna aliqua</p>
  <div class="vline" style="left:517px"></div>
  <div class="vline" style="left:833px"></div>
  <h5 style="left:562px;top:92px">Get in Touch</h5>
  <div class="contact-row" style="top:135px"><svg width="14" height="14" viewBox="0 0 14 14" fill="#fff"><path d="M3 1l2 3-1.5 1.5c1 2 2.5 3.5 4.5 4.5L9.5 8.5l3 2-1 2.5C6 13 1 8 1 2.5z"/></svg>+1 555 0142 7789</div>
  <div class="contact-row" style="top:170px"><svg width="16" height="12" viewBox="0 0 16 12" fill="#fff"><rect width="16" height="12" rx="1"/><path d="M1 1l7 6 7-6" stroke="#111" stroke-width="1.5" fill="none"/></svg>hello@brivanecomms.net</div>
  <div class="contact-row" style="top:207px"><svg width="12" height="16" viewBox="0 0 12 16" fill="#fff"><path d="M6 0a6 6 0 016 6c0 4-6 10-6 10S0 10 0 6a6 6 0 016-6z"/><circle cx="6" cy="6" r="2" fill="#111"/></svg>Brivane Communications, United States</div>
  <h5 style="left:876px;top:92px">Newsletter</h5>
  <p class="small" style="left:877px;top:124px;width:230px;line-height:26px">Lorem ipsum dolor sit amet, consectetur adipiscing elit.</p>
  <div class="email"><span>Email</span><b><svg width="20" height="20" viewBox="0 0 20 20" fill="#fff"><path d="M19 1L1 9l6 2 2 7 3-5 5 3z"/></svg></b></div>
  <div class="abs" style="left:98px;top:326px;width:1004px;height:1px;background:#555"></div>
  <div class="copyright">Copyrights@2023.Brivane Communications.All Rights Reserved</div>
</footer>

</body>
</html>
```